Business card design for online Mandarin Learning School

We need a business card design for our online language learning school called "Sunny Kite Academy for Mandarin Learning". Our existing website is https://www.sunnykiteacademy.com
We have our logo already. We would like to see our business card design that can make our online teaching services to be innovative, young, energetic and fun to learn. Prefer to have a certain level of color matching with our website. Apart from "Sunny Kite Academy", need to specifically state "for Mandarin Learning" as well on the business card.

```html
<!DOCTYPE html>
<html lang="en">
<head>
<meta charset="utf-8">
<title>Sunny Kite Academy – Business Card</title>
<link href="https://fonts.googleapis.com/css2?family=Marcellus&family=Lato:wght@400;700&display=swap" rel="stylesheet">
<style>
  :root {
    --teal: #1fa9b2;
    --teal-deep: #138f99;
    --coral: #e8675f;
    --grey-text: #8a8a8a;
    --ink: #2b2b2b;
    --rule: #c9c9c9;
    --paper: #fbfbfa;
    --stage: #e7e5e2;
    --back-top: #8a8f91;
  }
  * { box-sizing: border-box; margin: 0; padding: 0; }
  html, body { width: 1200px; height: 844px; overflow: hidden; }
  body {
    background: var(--stage);
    position: relative;
    font-family: "Lato", sans-serif;
  }
  .card {
    position: absolute;
    top: 273px;
    width: 520px;
    height: 298px;
    box-shadow: 0 10px 28px rgba(0,0,0,0.18);
  }
  /* Front */
  .card-front {
    left: 60px;
    background: var(--paper);
  }
  .brand {
    position: absolute;
    right: 34px;
    top: 48px;
    display: flex;
    align-items: center;
    gap: 10px;
    font-family: "Marcellus", serif;
    font-size: 24px;
    letter-spacing: 1.5px;
    color: var(--teal);
  }
  .brand-dot {
    width: 14px; height: 14px; border-radius: 50%;
    background: var(--coral);
  }
  .rule {
    position: absolute;
    height: 1px;
    background: var(--rule);
  }
  .rule-top { left: 210px; right: 30px; top: 98px; }
  .rule-mid { left: 150px; right: 30px; top: 122px; }
  .person {
    position: absolute;
    left: 32px;
    top: 150px;
  }
  .person-name {
    font-family: "Marcellus", serif;
    font-size: 20px;
    letter-spacing: 1px;
    text-transform: uppercase;
  }
  .person-name .first { color: var(--teal); }
  .person-name .last { color: var(--grey-text); }
  .person-role { font-size: 12px; color: var(--ink); margin-top: 1px; }
  .address {
    position: absolute;
    left: 32px;
    top: 204px;
    font-size: 12.5px;
    color: var(--ink);
  }
  .rule-contact { left: 32px; right: 200px; top: 228px; }
  .contact {
    position: absolute;
    left: 32px;
    top: 238px;
    font-size: 12.5px;
    color: var(--ink);
  }
  .contact .label { color: var(--teal); font-weight: 700; }
  .web {
    position: absolute;
    left: 32px;
    top: 258px;
    font-family: "Marcellus", serif;
    font-size: 17px;
    letter-spacing: 1.5px;
    text-transform: uppercase;
    color: var(--teal);
  }
  .web .prefix { color: var(--grey-text); }
  /* Back */
  .card-back {
    left: 620px;
    background: linear-gradient(180deg, var(--back-top) 0%, var(--teal) 55%, var(--teal-deep) 100%);
    color: #fff;
    display: flex;
    flex-direction: column;
    align-items: center;
    justify-content: center;
    text-align: center;
    overflow: hidden;
  }
  .back-wash {
    position: absolute; inset: 0;
    background: radial-gradient(ellipse at 40% 45%, rgba(255,255,255,0.10), rgba(255,255,255,0) 60%);
  }
  .back-title {
    position: relative;
    font-family: "Marcellus", serif;
    font-size: 34px;
    letter-spacing: 2.5px;
  }
  .back-tagline {
    position: relative;
    margin-top: 12px;
    font-size: 11px;
    letter-spacing: 1.2px;
    text-transform: uppercase;
  }
</style>
</head>
<body>
  <section class="card card-front" aria-label="Business card front">
    <div class="brand"><span class="brand-dot"></span>SUNNY KITE ACADEMY</div>
    <div class="rule rule-top"></div>
    <div class="rule rule-mid"></div>
    <div class="person">
      <p class="person-name"><span class="first">Daniel</span> <span class="last">Reyes</span></p>
      <p class="person-role">Managing Director</p>
    </div>
    <p class="address">18 Lantern Lane, Maple Bay, 20817</p>
    <div class="rule rule-contact"></div>
    <p class="contact"><span class="label">P:</span> 044-555 010 234 | <span class="label">E:</span> hello@sunnykiteacademy.com</p>
    <p class="web"><span class="prefix">www.</span>sunnykiteacademy.com</p>
  </section>

  <section class="card card-back" aria-label="Business card back">
    <div class="back-wash" role="img" aria-label="Soft teal background wash where a faint brand mark sits"></div>
    <h1 class="back-title">SUNNY KITE ACADEMY</h1>
    <p class="back-tagline">For Mandarin Learning</p>
  </section>
</body>
</html>
```